Menu Board 1000mmx500mm re-design

I would like to re-design exiting menu board 1000mmx500mm. Current board letters are bit to small to read. I would like to have pictures (attached) of the food offered on it and at the same time to create balance between pictures and size of the text to be easily readable. Fonts and colours are up to designer choice but prefer warm and bright colours rather anything dark.

Target Market(s)

Food industry

Industry/Entity Type

Food

Font styles to use
Other font styles liked:
• I leave font choice to designer

Colors
FFC000
F8CF3A
FAE287
FDF2CF
FEFAEE
F0912C
F2A743
F7CA91
FBE8D2
FDF5EE
EE7325
F08F49
F5BC92
FAE3D3
FDF4ED

Requirements
Must have
• Pictures + Text
Nice to have
• Balance between images and text.
Should not have
• Can't think of any

```html
<!DOCTYPE html>
<html lang="en">
<head>
<meta charset="UTF-8">
<title>Menu Board</title>
<link rel="stylesheet" href="https://fonts.googleapis.com/css2?family=Anton&family=Lobster&family=Montserrat:wght@500;800&family=Oswald:wght@500&family=Roboto+Condensed:wght@700&display=swap">
<style>
  :root {
    --orange-deep: #ee7325;
    --orange: #f0912c;
    --orange-light: #f2a743;
    --amber: #ffc000;
    --yellow: #f8c41a;
    --sun: #f9a51c;
    --brown: #5a2d12;
    --ink: #1c1c1c;
    --text: #2a2a2a;
    --white: #ffffff;
  }
  * { box-sizing: border-box; margin: 0; padding: 0; }
  html, body { width: 731px; height: 1200px; overflow: hidden; background: var(--white); }
  .board { position: relative; width: 731px; height: 1200px; overflow: hidden; background: var(--orange); font-family: "Montserrat", sans-serif; }

  .hero-bg { position: absolute; inset: 0 0 auto 0; height: 640px;
    background: radial-gradient(ellipse at 40% 30%, var(--amber) 0%, var(--sun) 40%, var(--orange) 75%, var(--orange-deep) 100%); }
  .hero-photo { position: absolute; left: 111px; top: 11px; width: 520px; height: 384px; border-radius: 48% 42% 38% 44% / 40% 38% 46% 44%;
    background: radial-gradient(ellipse at 45% 50%, #7a8f3a 0%, #c9a24a 45%, #efe0bf 75%, #e2c79a 100%); }

  .title { position: absolute; left: 0; right: 0; top: 405px; text-align: center;
    font-family: "Lobster", cursive; font-size: 178px; line-height: 1; color: var(--white);
    -webkit-text-stroke: 4px var(--brown); text-shadow: 6px 6px 0 var(--brown); letter-spacing: -2px; }

  .edge { position: absolute; left: 0; width: 731px; }
  .edge-menu { top: 600px; height: 600px; }
  .edge-sauce { top: 1004px; height: 196px; }

  .item { position: absolute; height: 92px; }
  .item-left { left: 19px; width: 280px; }
  .item-right { left: 365px; width: 290px; }
  .item-photo { position: absolute; left: 0; top: 0; width: 90px; height: 88px; border-radius: 50%;
    border: 3px solid var(--orange-deep); background: radial-gradient(circle at 50% 50%, #b5652a 0%, #d99a55 45%, #f2ece4 78%); }
  .item-name { position: absolute; left: 107px; top: 9px; font-weight: 800; font-size: 16.5px; line-height: 20px; color: #3a3a3a; letter-spacing: -0.1px; white-space: nowrap; }
  .item-desc { position: absolute; left: 107px; top: 31px; font-weight: 500; font-size: 12.4px; line-height: 15.5px; color: var(--text); width: 176px; }
  .item-right .item-desc { width: 196px; }
  .price { position: absolute; width: 37px; height: 34px; background: var(--orange-deep); color: var(--white);
    font-family: "Oswald", sans-serif; font-size: 17px; text-align: center; padding-top: 1px;
    clip-path: polygon(0 0, 100% 0, 100% 100%, 50% 78%, 0 100%); }
  .price-left { left: 302px; }
  .price-right { left: 657px; }
  .price sup { font-size: 9px; vertical-align: 6px; }

  .drink { position: absolute; top: 969px; height: 44px; background: var(--orange-light); color: var(--white);
    font-family: "Montserrat", sans-serif; font-weight: 800; font-size: 22px; line-height: 44px; border-radius: 2px 22px 22px 2px; white-space: nowrap; }
  .drink-water { left: 138px; width: 172px; padding-left: 24px; }
  .drink-cans { left: 358px; width: 256px; padding-left: 8px; }
  .drink-price { position: absolute; right: 0; top: 0; width: 42px; height: 44px; border-radius: 50%; background: var(--orange-deep);
    border: 2px solid var(--white); font-family: "Oswald", sans-serif; font-weight: 500; font-size: 16px; text-align: center; line-height: 40px; }
  .drink-price sup { font-size: 8px; vertical-align: 5px; }

  .sauces-title { position: absolute; left: 0; right: 0; top: 1064px; text-align: center; font-family: "Anton", sans-serif; font-size: 48px; line-height: 1; color: var(--ink); }
  .sauce-row { position: absolute; left: 0; right: 0; display: flex; justify-content: center; gap: 18px; }
  .sauce-row.one { top: 1129px; }
  .sauce-row.two { top: 1168px; }
  .sauce { display: flex; align-items: center; gap: 12px; font-family: "Roboto Condensed", sans-serif; font-weight: 700; font-size: 21px; color: var(--ink); }
  .tick { width: 24px; height: 24px; }
</style>
</head>
<body>
<main class="board">
  <div class="hero-bg"></div>
  <div class="hero-photo" role="img" aria-label="Photo of a grilled wrap cut in half, filled with greens, tomato and onion"></div>
  <h1 class="title">Menu</h1>

  <svg class="edge edge-menu" viewBox="0 0 731 600" preserveAspectRatio="none" aria-hidden="true">
    <polygon fill="var(--amber)" points="0,45 40,38 70,42 110,30 150,36 190,28 230,40 270,26 300,36 340,10 380,22 420,4 460,18 500,8 520,22 560,0 600,14 640,22 680,30 731,36 731,600 0,600"/>
    <polygon fill="var(--white)" points="0,52 35,46 60,52 100,40 140,48 180,38 220,50 260,36 300,46 340,24 380,34 420,20 460,30 500,22 530,30 565,18 600,26 640,34 690,40 731,44 731,600 0,600"/>
  </svg>

  <div class="item item-left" style="top:659px;">
    <div class="item-photo" role="img" aria-label="Photo of a chicken ciabatta sandwich"></div>
    <div class="item-name">CIABATTA</div>
    <div class="item-desc">Roti Chicken, Rucola, Caramelized Onions, Tomato, Fresh Onion</div>
  </div>
  <div class="price price-left" style="top:662px;"><sup>£</sup>6</div>

  <div class="item item-left" style="top:763px;">
    <div class="item-photo" role="img" aria-label="Photo of roasted chicken wings"></div>
    <div class="item-name" style="top:16px;">ROTI WINGS</div>
    <div class="item-desc" style="top:38px;">Roti Chicken Wings &amp; Roosted Potatoes</div>
  </div>
  <div class="price price-left" style="top:773px;"><sup>£</sup>9</div>

  <div class="item item-left" style="top:870px;">
    <div class="item-photo" role="img" aria-label="Photo of half a roast chicken with rice"></div>
    <div class="item-name" style="top:12px;">1/2 CHICKEN BOX</div>
    <div class="item-desc" style="top:45px;">Roti Chicken, Veggie Rice &amp; Salad</div>
  </div>
  <div class="price price-left" style="top:876px;"><sup>£</sup>14</div>

  <div class="item item-right" style="top:659px;">
    <div class="item-photo" role="img" aria-label="Photo of a grilled chicken wrap"></div>
    <div class="item-name">WRAP</div>
    <div class="item-desc">Roti Chicken, Crunchy Slaw, Tomato, Fresh Onion &amp; Sauce of your choice</div>
  </div>
  <div class="price price-right" style="top:664px;"><sup>£</sup>8</div>

  <div class="item item-right" style="top:767px;">
    <div class="item-photo" role="img" aria-label="Photo of a quarter chicken with rice in a bowl"></div>
    <div class="item-name" style="top:13px;">1/4 CHICKEN BOX</div>
    <div class="item-desc" style="top:35px;width:150px;">Roti Chicken, Veggie Rice &amp; Salad</div>
  </div>
  <div class="price price-right" style="top:773px;"><sup>£</sup>10</div>

  <div class="item item-right" style="top:866px;">
    <div class="item-photo" role="img" aria-label="Photo of golden roasted potatoes"></div>
    <div class="item-name" style="top:18px;line-height:22px;">ROASTED<br>POTATOES</div>
    <div class="item-desc" style="top:69px;">Thyme &amp; Garlic</div>
  </div>
  <div class="price price-right" style="top:880px;"><sup>£</sup>2.5</div>

  <div class="drink drink-water">WATER<span class="drink-price"><sup>£</sup>1</span></div>
  <div class="drink drink-cans">CANS &amp; JUICES<span class="drink-price"><sup>£</sup>1.8</span></div>

  <svg class="edge edge-sauce" viewBox="0 0 731 196" preserveAspectRatio="none" aria-hidden="true">
    <polygon fill="var(--yellow)" points="0,22 40,14 80,24 120,10 160,26 200,12 240,20 280,34 320,20 360,28 400,14 440,24 480,40 520,26 560,34 600,18 640,26 690,12 731,6 731,196 0,196"/>
  </svg>

  <h2 class="sauces-title">SAUCES</h2>
  <div class="sauce-row one">
    <span class="sauce"><svg class="tick" viewBox="0 0 24 24" aria-hidden="true"><circle cx="12" cy="12" r="12" fill="var(--orange-deep)"/><path d="M7 12.5l3.2 3.2L17 9" fill="none" stroke="var(--white)" stroke-width="2.4" stroke-linecap="round" stroke-linejoin="round"/></svg>SIGNATURE</span>
    <span class="sauce"><svg class="tick" viewBox="0 0 24 24" aria-hidden="true"><circle cx="12" cy="12" r="12" fill="var(--orange-deep)"/><path d="M7 12.5l3.2 3.2L17 9" fill="none" stroke="var(--white)" stroke-width="2.4" stroke-linecap="round" stroke-linejoin="round"/></svg>GARLIC MAYO</span>
    <span class="sauce"><svg class="tick" viewBox="0 0 24 24" aria-hidden="true"><circle cx="12" cy="12" r="12" fill="var(--orange-deep)"/><path d="M7 12.5l3.2 3.2L17 9" fill="none" stroke="var(--white)" stroke-width="2.4" stroke-linecap="round" stroke-linejoin="round"/></svg>BBQ</span>
  </div>
  <div class="sauce-row two">
    <span class="sauce"><svg class="tick" viewBox="0 0 24 24" aria-hidden="true"><circle cx="12" cy="12" r="12" fill="var(--orange-deep)"/><path d="M7 12.5l3.2 3.2L17 9" fill="none" stroke="var(--white)" stroke-width="2.4" stroke-linecap="round" stroke-linejoin="round"/></svg>SWEET CHILLI</span>
    <span class="sauce"><svg class="tick" viewBox="0 0 24 24" aria-hidden="true"><circle cx="12" cy="12" r="12" fill="var(--orange-deep)"/><path d="M7 12.5l3.2 3.2L17 9" fill="none" stroke="var(--white)" stroke-width="2.4" stroke-linecap="round" stroke-linejoin="round"/></svg>PIRI PIRI</span>
  </div>
</main>
</body>
</html>
```